Q7M Electrical Systems Inc Business Cards

Target Market(s)

Customers

Industry/Entity Type

Construction - Electrical

Contact Information for Business Card

Company Name, Address, Phone, and email address

Font styles to use
Sans Serif

Colors
0054AA
0677BA
7BADD7
CADEEF
E8F1F8

Requirements
Must have
• we would like to use the same design that we had our vehicles wrapped
Nice to have
• The design that we used on our trucks

```html
<!DOCTYPE html>
<html lang="en">
<head>
<meta charset="utf-8">
<title>Q7M Electrical Systems Inc – Business Cards</title>
<link rel="stylesheet" href="https://fonts.googleapis.com/css2?family=Jost:wght@400;500&display=swap">
<style>
  :root {
    --navy: #061a36;
    --silver: #c1c6c9;
    --white: #ffffff;
    --backdrop: #c1c6c9;
  }
  * { margin: 0; padding: 0; box-sizing: border-box; }
  html, body {
    width: 1200px; height: 1200px; overflow: hidden;
    background: var(--backdrop);
    font-family: "Jost", "Futura", sans-serif;
  }
  .card {
    position: absolute; left: 180px;
    width: 840px; height: 480px;
    background: var(--white); overflow: hidden;
  }
  .card--front { top: 70px; }
  .card--back { top: 650px; }
  .card__art { position: absolute; inset: 0; width: 840px; height: 480px; }

  .wordmark {
    position: absolute; color: var(--navy);
    font-weight: 500; text-align: center; line-height: 1;
  }
  .wordmark__initials { display: block; font-size: 76px; letter-spacing: 2px; }
  .wordmark__name { display: block; font-size: 34px; letter-spacing: 0.5px; margin-top: 6px; }
  .wordmark__suffix { display: block; font-size: 12px; letter-spacing: 10.4px; margin-top: 4px; padding-left: 10px; }
  .card--front .wordmark { left: 232px; top: 148px; width: 272px; }
  .card--back .wordmark { left: 508px; top: 60px; width: 272px; }

  .contact { position: absolute; left: 34px; top: 204px; list-style: none; color: var(--navy); }
  .contact__item { display: flex; align-items: flex-start; font-size: 29px; line-height: 40px; margin-bottom: 10px; }
  .contact__icon { width: 32px; height: 32px; margin: 4px 14px 0 0; flex: none; }
</style>
</head>
<body>

<section class="card card--front" aria-label="Card front">
  <svg class="card__art" viewBox="0 0 840 480" aria-hidden="false">
    <path class="band band--silver" fill="var(--silver)"
      d="M604,0 L718,0 C690,250 560,440 100,480 L0,480 L0,462 C380,440 570,300 604,0 Z"/>
    <path class="stripe stripe--white" fill="none" stroke="var(--white)" stroke-width="6"
      d="M650,0 C625,240 520,390 420,410"/>
    <path class="stripe stripe--white" fill="none" stroke="var(--white)" stroke-width="5"
      d="M420,410 C300,450 160,472 20,478"/>
    <path class="panel panel--navy" fill="var(--navy)" role="img"
      aria-label="Navy panel with faint circuit-board line pattern"
      d="M718,0 L840,0 L840,480 L100,480 C560,440 690,250 718,0 Z"/>
  </svg>
  <div class="wordmark">
    <span class="wordmark__initials">Q7M</span>
    <span class="wordmark__name">ELECTRICAL</span>
    <span class="wordmark__suffix">SYSTEMS INC.</span>
  </div>
</section>

<section class="card card--back" aria-label="Card back">
  <svg class="card__art" viewBox="0 0 840 480">
    <path class="band band--silver" fill="var(--silver)"
      d="M840,270 L840,304 C560,310 400,360 312,480 L296,480 C380,330 560,280 840,270 Z"/>
    <path class="stripe stripe--white" fill="none" stroke="var(--white)" stroke-width="4"
      d="M800,276 C600,290 440,330 360,400"/>
    <rect class="bar bar--navy" x="0" y="462" width="320" height="18" fill="var(--navy)"/>
    <path class="panel panel--navy" fill="var(--navy)" role="img"
      aria-label="Navy panel with faint circuit-board line pattern"
      d="M840,304 L840,480 L312,480 C400,360 560,310 840,304 Z"/>
  </svg>

  <div class="wordmark">
    <span class="wordmark__initials">Q7M</span>
    <span class="wordmark__name">ELECTRICAL</span>
    <span class="wordmark__suffix">SYSTEMS INC.</span>
  </div>

  <ul class="contact">
    <li class="contact__item">
      <svg class="contact__icon" viewBox="0 0 32 32" aria-label="Address">
        <circle cx="16" cy="16" r="16" fill="var(--navy)"/>
        <path d="M16,7 a7,7 0 0 1 7,7 c0,5 -7,11 -7,11 s-7,-6 -7,-11 a7,7 0 0 1 7,-7 z" fill="var(--white)"/>
        <circle cx="16" cy="14" r="3" fill="var(--navy)"/>
      </svg>
      <span>412 Harbor Ridge Way # 208<br>Lakeview Springs, FL 32790</span>
    </li>
    <li class="contact__item">
      <svg class="contact__icon" viewBox="0 0 32 32" aria-label="Phone">
        <circle cx="16" cy="16" r="16" fill="var(--navy)"/>
        <path d="M10,8 l4,0 l1.5,5 l-2.5,2 c1,2.5 3,4.5 5.5,5.5 l2,-2.5 l5,1.5 l0,4 c-9,1 -16,-6 -15.5,-15.5 z" fill="var(--white)"/>
      </svg>
      <span>407 555 0148</span>
    </li>
    <li class="contact__item">
      <svg class="contact__icon" viewBox="0 0 32 32" aria-label="Email">
        <circle cx="16" cy="16" r="16" fill="var(--navy)"/>
        <rect x="8" y="10" width="16" height="12" rx="1" fill="var(--white)"/>
        <path d="M8,11 l8,6 l8,-6" fill="none" stroke="var(--navy)" stroke-width="1.6"/>
      </svg>
      <span>info@q7melectric.com</span>
    </li>
  </ul>
</section>

</body>
</html>
```